TrueGrindz Complete Stationery - Logo already designed

I already have the logo designed see attached. I need have a full set of stationary and business card designed for printing. I have attached an example of what I mean.

Please feel free to be creative. Also you can use the X in the logo by its self if you think it will work.

My details:

Name: Corwin Lestak
Social media handles: @corwinlestak
W: corwinlestak.com
E: info@corwinlestak.com
​P: 08 7493 5286
PO Box 7382, Marrowdale 6027
ABN 83 402 719 265

Target Market(s)

Anyone looking to be inspired.

Industry/Entity Type

Business

Font styles to use
Sans Serif

Colors
fbee3e
000000

Requirements
Must have
• My details:
• Name: Corwin Lestak
• Social media handles: @corwinlestak
• W: corwinlestak.com
• E: info@corwinlestak.com
• ​P: 08 7493 5286
• PO Box 7382, Marrowdale 6027
• ABN 83 402 719 265
Nice to have
• Something a little different
Should not have
• must not look tacky.

```html
<!DOCTYPE html>
<html lang="en">
<head>
<meta charset="utf-8">
<title>TrueGrindz Business Card</title>
<link rel="stylesheet" href="https://fonts.googleapis.com/css2?family=Open+Sans:wght@400;800&family=Michroma&display=swap">
<style>
  :root {
    --yellow: #fbd42e;
    --yellow-bright: #fbee3e;
    --gold-dark: #6f5e1c;
    --ink: #111111;
    --charcoal: #363434;
    --white: #ffffff;
    --backdrop: #b9b9b9;
    --backdrop-light: #d6d6d6;
  }
  html, body {
    margin: 0;
    padding: 0;
    width: 1200px;
    height: 900px;
    overflow: hidden;
  }
  body {
    background: linear-gradient(160deg, var(--backdrop-light), var(--backdrop));
    position: relative;
    font-family: "Open Sans", sans-serif;
  }
  .card {
    position: absolute;
    width: 700px;
    height: 400px;
    border-radius: 30px;
    overflow: hidden;
    background: var(--white);
    box-shadow: 0 10px 24px rgba(0,0,0,0.22);
  }
  .card--front { left: 420px; top: 40px; }
  .card--back  { left: 80px;  top: 470px; }

  .card__art {
    position: absolute;
    inset: 0;
    width: 100%;
    height: 100%;
  }

  .brand-name {
    font-family: "Open Sans", sans-serif;
    font-weight: 800;
    color: var(--ink);
    letter-spacing: -1px;
    margin: 0;
    line-height: 1;
  }
  .front__brand {
    position: absolute;
    left: 90px;
    top: 120px;
  }
  .front__brand .brand-name { font-size: 70px; }
  .front__web {
    font-family: "Michroma", sans-serif;
    font-size: 15px;
    letter-spacing: 4px;
    color: var(--ink);
    margin: 18px 0 0 4px;
  }

  .back__brand {
    position: absolute;
    left: 46px;
    top: 152px;
  }
  .back__brand .brand-name { font-size: 44px; }
  .back__person {
    font-family: "Michroma", sans-serif;
    font-size: 21px;
    color: var(--ink);
    margin: 12px 0 0 0;
    letter-spacing: 1px;
  }

  .contact-list {
    position: absolute;
    left: 380px;
    top: 92px;
    margin: 0;
    padding: 0;
    list-style: none;
    color: var(--white);
    font-size: 22px;
    line-height: 1.2;
  }
  .contact-list li {
    display: flex;
    align-items: flex-start;
    gap: 14px;
    margin-bottom: 8px;
  }
  .contact-icon {
    flex: 0 0 auto;
    width: 26px;
    height: 26px;
    margin-top: 1px;
  }
</style>
</head>
<body>

  <section class="card card--front" aria-label="Business card front">
    <svg class="card__art" viewBox="0 0 700 400" aria-hidden="true">
      <defs>
        <linearGradient id="gold-sweep" x1="0" y1="0" x2="1" y2="0">
          <stop offset="0" stop-color="var(--yellow)"/>
          <stop offset="0.55" stop-color="#e9c12c"/>
          <stop offset="1" stop-color="var(--gold-dark)"/>
        </linearGradient>
        <linearGradient id="gold-fold" x1="0" y1="0" x2="1" y2="0">
          <stop offset="0" stop-color="#f7cd2a"/>
          <stop offset="1" stop-color="#8c7522"/>
        </linearGradient>
      </defs>
      <path d="M360 0 L700 0 L700 400 L430 400 C560 330 640 200 360 0 Z" fill="url(#gold-sweep)"/>
      <path d="M520 120 C640 170 680 150 700 140 L700 400 L600 400 C630 300 600 190 520 120 Z" fill="url(#gold-fold)" opacity="0.85"/>
    </svg>
    <div class="front__brand">
      <p class="brand-name">TrueGrindz</p>
      <p class="front__web">www.corwinlestak.com</p>
    </div>
  </section>

  <section class="card card--back" aria-label="Business card back">
    <svg class="card__art" viewBox="0 0 700 400" aria-hidden="true">
      <polygon points="390,0 700,0 700,400 260,400" fill="var(--charcoal)"/>
    </svg>
    <div class="back__brand">
      <p class="brand-name">TrueGrindz</p>
      <p class="back__person">Corwin Lestak</p>
    </div>
    <ul class="contact-list">
      <li>
        <svg class="contact-icon" viewBox="0 0 26 26" aria-hidden="true">
          <circle cx="13" cy="13" r="11.5" fill="none" stroke="var(--yellow)" stroke-width="2"/>
          <path d="M13 6 a4.5 4.5 0 0 1 4.5 4.5 c0 3.5 -4.5 8.5 -4.5 8.5 s-4.5 -5 -4.5 -8.5 A4.5 4.5 0 0 1 13 6 Z" fill="var(--yellow)"/>
          <circle cx="13" cy="10.5" r="1.7" fill="var(--charcoal)"/>
        </svg>
        <span>PO Box 7382,<br>Marrowdale 6027</span>
      </li>
      <li>
        <svg class="contact-icon" viewBox="0 0 26 26" aria-hidden="true">
          <circle cx="13" cy="13" r="11.5" fill="none" stroke="var(--yellow)" stroke-width="2"/>
          <path d="M9 7 l3 0 l1 4 l-2 1.5 c1 2 2 3 3.5 3.5 l1.5 -2 l4 1 l0 3 c-6 1 -12 -5 -11 -11 Z" fill="var(--yellow)"/>
        </svg>
        <span>08 7493 5286</span>
      </li>
      <li>
        <svg class="contact-icon" viewBox="0 0 26 26" aria-hidden="true">
          <circle cx="13" cy="13" r="11.5" fill="none" stroke="var(--yellow)" stroke-width="2"/>
          <rect x="6.5" y="8.5" width="13" height="9" fill="none" stroke="var(--yellow)" stroke-width="1.6"/>
          <path d="M6.5 8.5 L13 14 L19.5 8.5" fill="none" stroke="var(--yellow)" stroke-width="1.6"/>
        </svg>
        <span>info@corwinlestak.com</span>
      </li>
      <li>
        <svg class="contact-icon" viewBox="0 0 26 26" aria-hidden="true">
          <circle cx="13" cy="13" r="11.5" fill="none" stroke="var(--yellow)" stroke-width="2"/>
        </svg>
        <span>@corwinlestak</span>
      </li>
      <li>
        <svg class="contact-icon" viewBox="0 0 26 26" aria-hidden="true">
          <circle cx="13" cy="13" r="11.5" fill="var(--yellow)"/>
          <ellipse cx="13" cy="13" rx="4.5" ry="11" fill="none" stroke="var(--charcoal)" stroke-width="1.3"/>
          <line x1="2" y1="13" x2="24" y2="13" stroke="var(--charcoal)" stroke-width="1.3"/>
        </svg>
        <span>corwinlestak.com</span>
      </li>
    </ul>
  </section>

</body>
</html>
```